business card design - photography

I am a fine art photographer. I would like to approach galleries to exhibit my work and need a business card.

The card should convey creativity and simplicity.
I would like a double sided card.

Some options:
1. An all white card with raised or embossed text or design to create a tactile finish.
2. a white and dark grey design would also work well.
3. Would be great to use my name as part of the design but not essential.
4. My name and title on the front, other details on the back of card.

The final design should be simple, minimal, elegant and innovative.
Being minimal, it will be more about texture, text size and placement.

examples of designs I would prefer provided here:
http://plimvarka.com/ideas/40-quiet-and-refined-card-layouts

I'm also open to other designs that may be unusual and unique.

Love this:
http://www.snapvelo.com/pics/morningverselog/583014927
Updates

I have uploaded a psd file after playing around in photoshop with various fonts.  I like the font (which I downloaded from glyphmorra.com called Arual) but the design probably needs some refining.  I hope this helps.  If you'd like me to change the format of the file, please let me know.

Ilvane

Target Market(s)

Art Gallery owners/administrators and customers.

Industry/Entity Type

Business

Requirements
Must have
• A unique look.

Matte, silky finish or heavy textured stock. Double-sided card.

Front:
my name
photography by

Back:
phone no
email
web address
Nice to have
• Letterpress
embrossed
Clean fonts
Should not have
• Do not use illustrations of cameras or lenses.
No frames around the card edge.

```html
<!DOCTYPE html>
<html lang="en">
<head>
<meta charset="utf-8">
<title>Ilvane Dessault Photography – Business Card</title>
<link rel="stylesheet" href="https://fonts.googleapis.com/css2?family=Montserrat:ital,wght@0,700;1,700&display=swap">
<style>
  :root {
    --stage: #3b3b3d;
    --card-centre: #3a3a3c;
    --card-edge: #1a1a1b;
    --brand-red: #e01e26;
    --ink-white: #f2f2f2;
    --ink-soft: #d8d8d8;
  }
  * { margin: 0; padding: 0; box-sizing: border-box; }
  html, body {
    width: 1200px;
    height: 534px;
    overflow: hidden;
    background: var(--stage);
    font-family: "Montserrat", Arial, sans-serif;
  }
  .stage {
    position: relative;
    width: 1200px;
    height: 534px;
  }
  .card {
    position: absolute;
    top: 119px;
    width: 517px;
    height: 294px;
    background: radial-gradient(ellipse at 50% 42%, var(--card-centre) 0%, #2a2a2b 55%, var(--card-edge) 100%);
    box-shadow: 0 4px 14px rgba(0, 0, 0, 0.45);
  }
  .card--front { left: 62px; }
  .card--back { left: 622px; }

  .wordmark {
    position: absolute;
    display: flex;
    flex-direction: column;
    align-items: flex-end;
  }
  .wordmark__name {
    color: var(--brand-red);
    font-weight: 700;
    line-height: 1;
    white-space: nowrap;
  }
  .wordmark__title {
    color: var(--ink-white);
    font-weight: 700;
    letter-spacing: 0.06em;
    line-height: 1;
  }

  .card--front .wordmark {
    left: 50%;
    top: 112px;
    transform: translateX(-50%);
  }
  .card--front .wordmark__name { font-size: 40px; }
  .card--front .wordmark__title { font-size: 15px; margin-top: 4px; }

  .card--back .wordmark {
    left: 30px;
    top: 218px;
  }
  .card--back .wordmark__name { font-size: 20px; }
  .card--back .wordmark__title { font-size: 8px; margin-top: 3px; }

  .contact {
    position: absolute;
    left: 275px;
    top: 220px;
    list-style: none;
    color: var(--ink-soft);
    font-size: 10.5px;
    font-style: italic;
    font-weight: 700;
    letter-spacing: 0.05em;
    text-transform: uppercase;
  }
  .contact li { line-height: 17px; white-space: nowrap; }
  .contact__label { font-size: 8.5px; margin-right: 3px; }
</style>
</head>
<body>
  <main class="stage">
    <section class="card card--front" aria-label="Card front">
      <div class="wordmark">
        <span class="wordmark__name">Ilvane Dessault</span>
        <span class="wordmark__title">PHOTOGRAPHY</span>
      </div>
    </section>

    <section class="card card--back" aria-label="Card back">
      <div class="wordmark">
        <span class="wordmark__name">Ilvane Dessault</span>
        <span class="wordmark__title">PHOTOGRAPHY</span>
      </div>
      <ul class="contact">
        <li><span class="contact__label">Phone:</span>0491 570 118</li>
        <li><span class="contact__label">Email:</span>idessault@mailvessel.com</li>
        <li><span class="contact__label">Website:</span>www.ilvanedessault.com</li>
      </ul>
    </section>
  </main>
</body>
</html>
```